Brindle 48 Focus Wheel

We need a professional **framework wheel diagram** designed for our detection dog training manual.

Our business is **Brindle 48 Dog Training**, and this graphic represents our **Detection Training Model**.

Please use the **attached reference images** as a guide for the structure and layout of the wheel.

### What we need

1. **Full wheel graphic**

* Clean circular framework wheel
* Similar structure to the attached example
* Clear sections and text
* Professional training manual style
* Transparent background

2. **Individual segment pieces**

We also need the **inner sections broken into separate pieces** (like the second reference image).

This will allow us to place each section on different pages of the manual when explaining the concepts.

Each piece should look like a **slice of the wheel**.

### Style

The design should look:

• Professional
• Clean and modern
• Structured and easy to read
• Suitable for a training manual

Avoid cartoon styles or clipart.

### Colours

Please use our brand colour palette (see attached image):

* Dark navy blue
* Steel blue
* Light blue
* White
* Light grey
* Dark grey

### Files required

Final files must include:

* Vector files (AI or EPS)
* Transparent PNG
* High-resolution PDF

Please also provide **each segment exported individually**

```html
<!DOCTYPE html>
<html lang="en">
<head>
<meta charset="utf-8">
<title>Brindle 48 Focus Wheel</title>
<link rel="stylesheet" href="https://fonts.googleapis.com/css2?family=Montserrat:wght@300;400;500&display=swap">
<style>
  :root {
    --page: #ffffff;
    --ring-light: #d1d3d4;
    --segment-grey: #a7a9ac;
    --segment-blue: #67aacd;
    --line: #1e1e1e;
    --ink: #262626;
    --hub: #ffffff;
  }
  html, body {
    margin: 0;
    padding: 0;
    width: 1200px;
    height: 1200px;
    overflow: hidden;
    background: var(--page);
  }
  .wheel {
    display: block;
    width: 1200px;
    height: 1200px;
    font-family: "Montserrat", sans-serif;
  }
  .ring-light { fill: var(--ring-light); }
  .band-grey { fill: var(--segment-grey); }
  .band-blue { fill: var(--segment-blue); }
  .hub { fill: var(--hub); stroke: var(--segment-grey); stroke-width: 2; }
  .edge { fill: none; stroke: var(--line); stroke-width: 1.6; }
  .divider { stroke: var(--line); stroke-width: 1.6; }
  .ring-title {
    fill: var(--ink);
    font-size: 34px;
    font-weight: 400;
    letter-spacing: 6px;
  }
  .foundation-title {
    fill: var(--ink);
    font-size: 26px;
    font-weight: 400;
    letter-spacing: 4px;
  }
  .core-title {
    fill: var(--ink);
    font-size: 21px;
    font-weight: 400;
    letter-spacing: 4px;
  }
  .area-label {
    fill: var(--ink);
    font-size: 28px;
    font-weight: 400;
    letter-spacing: 1px;
    text-anchor: middle;
  }
  .foundation-label {
    fill: var(--ink);
    font-size: 18.5px;
    font-weight: 400;
    text-anchor: middle;
  }
  .brand-name {
    fill: var(--ink);
    font-size: 17px;
    font-weight: 500;
    text-anchor: middle;
  }
  .brand-ring { fill: none; stroke: var(--ink); stroke-width: 1.2; }
</style>
</head>
<body>
<svg class="wheel" viewBox="0 0 1200 1200" xmlns="http://www.w3.org/2000/svg" aria-label="Brindle 48 Focus Wheel">
  <defs>
    <path id="arc-area-top" d="M 65 600 A 535 535 0 0 1 1135 600"/>
    <path id="arc-area-bottom" d="M 41 600 A 559 559 0 0 0 1159 600"/>
    <path id="arc-dog-top" d="M 295 600 A 305 305 0 0 1 905 600"/>
    <path id="arc-handler-bottom" d="M 276 600 A 324 324 0 0 0 924 600"/>
    <path id="arc-core-top" d="M 512 600 A 88 88 0 0 1 688 600"/>
    <path id="arc-core-bottom" d="M 496 600 A 104 104 0 0 0 704 600"/>
  </defs>

  <!-- Operational capability area ring -->
  <circle class="ring-light" cx="600" cy="600" r="583"/>
  <path class="band-grey" d="M 89 600 A 511 511 0 0 1 1111 600 Z"/>
  <path class="band-blue" d="M 89 600 A 511 511 0 0 0 1111 600 Z"/>

  <!-- Foundations ring -->
  <circle class="ring-light" cx="600" cy="600" r="335"/>
  <path class="band-blue" d="M 306 600 A 294 294 0 0 1 894 600 Z"/>
  <path class="band-grey" d="M 306 600 A 294 294 0 0 0 894 600 Z"/>

  <!-- Core -->
  <circle class="ring-light" cx="600" cy="600" r="121"/>

  <!-- Edges -->
  <circle class="edge" cx="600" cy="600" r="511"/>
  <circle class="edge" cx="600" cy="600" r="335"/>
  <circle class="edge" cx="600" cy="600" r="294"/>
  <circle class="edge" cx="600" cy="600" r="121"/>

  <!-- Outer dividers -->
  <g class="outer-dividers">
    <line class="divider" x1="89" y1="600" x2="265" y2="600"/>
    <line class="divider" x1="935" y1="600" x2="1111" y2="600"/>
    <line class="divider" x1="329" y1="403" x2="186.6" y2="299.5"/>
    <line class="divider" x1="496.5" y1="281.4" x2="442.1" y2="114"/>
    <line class="divider" x1="703.5" y1="281.4" x2="757.9" y2="114"/>
    <line class="divider" x1="871" y1="403" x2="1013.4" y2="299.5"/>
    <line class="divider" x1="836.9" y1="836.9" x2="961.3" y2="961.3"/>
    <line class="divider" x1="600" y1="935" x2="600" y2="1111"/>
    <line class="divider" x1="363.1" y1="836.9" x2="238.7" y2="961.3"/>
  </g>

  <!-- Inner dividers -->
  <g class="inner-dividers">
    <line class="divider" x1="306" y1="600" x2="479" y2="600"/>
    <line class="divider" x1="721" y1="600" x2="894" y2="600"/>
    <line class="divider" x1="502.1" y1="528.9" x2="362.2" y2="427.1"/>
    <line class="divider" x1="562.6" y1="484.9" x2="509.1" y2="320.4"/>
    <line class="divider" x1="637.4" y1="484.9" x2="690.9" y2="320.4"/>
    <line class="divider" x1="697.9" y1="528.9" x2="837.8" y2="427.1"/>
    <line class="divider" x1="685.6" y1="685.6" x2="807.9" y2="807.9"/>
    <line class="divider" x1="600" y1="721" x2="600" y2="894"/>
    <line class="divider" x1="514.4" y1="685.6" x2="392.1" y2="807.9"/>
  </g>

  <!-- Ring titles -->
  <text class="ring-title"><textPath href="#arc-area-top" startOffset="50%" text-anchor="middle">OPERATIONAL CAPABILITY AREA</textPath></text>
  <text class="ring-title"><textPath href="#arc-area-bottom" startOffset="50%" text-anchor="middle">OPERATIONAL CAPABILITY AREA</textPath></text>
  <text class="foundation-title"><textPath href="#arc-dog-top" startOffset="50%" text-anchor="middle">DOG FOUNDATIONS</textPath></text>
  <text class="foundation-title"><textPath href="#arc-handler-bottom" startOffset="50%" text-anchor="middle">HANDLER FOUNDATIONS</textPath></text>

  <!-- Operational capability labels -->
  <g class="area-labels">
    <text class="area-label" x="600" y="187" transform="rotate(-72 600 600)">INTEGRITY</text>
    <text class="area-label" x="600" y="187" transform="rotate(-36 600 600)">DEVELOPMENT</text>
    <text class="area-label" x="600" y="187">DISTRACTIONS</text>
    <text class="area-label" x="600" y="187" transform="rotate(36 600 600)">BEHAVIOUR</text>
    <text class="area-label" x="600" y="187" transform="rotate(72 600 600)">HANDLER</text>
    <text class="area-label" x="600" y="1033" transform="rotate(67.5 600 600)">DEPLOYMENT</text>
    <text class="area-label" x="600" y="1033" transform="rotate(22.5 600 600)">REINFORCEMENT</text>
    <text class="area-label" x="600" y="1033" transform="rotate(-22.5 600 600)">SEARCH METHOD</text>
    <text class="area-label" x="600" y="1033" transform="rotate(-67.5 600 600)">TARGET ODOUR</text>
  </g>

  <!-- Dog foundations -->
  <g class="dog-foundations">
    <text class="foundation-label" x="408" y="540"><tspan x="408" dy="0">GENERIC</tspan><tspan x="408" dy="24">SUITABILITY</tspan></text>
    <text class="foundation-label" x="476" y="405"><tspan x="476" dy="0">HEALTH &amp;</tspan><tspan x="476" dy="24">PHYSICAL</tspan><tspan x="476" dy="24">WELLBEING</tspan></text>
    <text class="foundation-label" x="598" y="362"><tspan x="598" dy="0">ENGAGE-</tspan><tspan x="598" dy="24">MENT</tspan><tspan x="598" dy="24">RELATION</tspan><tspan x="598" dy="24">-SHIP</tspan></text>
    <text class="foundation-label" x="718" y="414"><tspan x="718" dy="0">REWARD</tspan><tspan x="718" dy="24">VALUE</tspan></text>
    <text class="foundation-label" x="783" y="540"><tspan x="783" dy="0">AROUSAL</tspan><tspan x="783" dy="24">REGULATION</tspan></text>
  </g>

  <!-- Handler foundations -->
  <g class="handler-foundations">
    <text class="foundation-label" x="407" y="670"><tspan x="407" dy="0">DOG</tspan><tspan x="407" dy="24">SAFETY</tspan></text>
    <text class="foundation-label" x="523" y="781"><tspan x="523" dy="0">SEARCH</tspan><tspan x="523" dy="24">COVERAGE</tspan></text>
    <text class="foundation-label" x="700" y="768"><tspan x="700" dy="0">MINIMAL</tspan><tspan x="700" dy="24">NECESSARY</tspan><tspan x="700" dy="24">INVOLVEMENT</tspan></text>
    <text class="foundation-label" x="790" y="670"><tspan x="790" dy="0">READ THE</tspan><tspan x="790" dy="24">DOG</tspan></text>
  </g>

  <!-- Core -->
  <text class="core-title"><textPath href="#arc-core-top" startOffset="50%" text-anchor="middle">DETECTION</textPath></text>
  <text class="core-title"><textPath href="#arc-core-bottom" startOffset="50%" text-anchor="middle">CAPABILITIES</textPath></text>
  <circle class="hub" cx="600" cy="600" r="72"/>
  <circle class="brand-ring" cx="600" cy="600" r="60"/>
  <text class="brand-name" x="600" y="606">Brindle 48</text>
</svg>
</body>
</html>
```